Packaging Design for Vitorique a Company Providing a Convenient and Complete Alternative to Food

We need a packaging and label design for Vitorique. Vitorique stands for nutrient balance and it is a meal alternative that comes in a powder that has all the nutrients needed for a complete and balanced meal. Vitorique would be used by people that are hungry but don't have time to cook, are in a rush, or simply want to get the healthiest meal they can as conveniently as possible. We were thinking of using a modern and simple design that would attract consumers in the 22-28 age bracket. I want the packaging to be cool and attractive using blue and orange/red (an orangey red) since those are the colors of the logo

Now that being said, Vitorique is more about a lifestyle than the product itself. The website still doesn't reflect this because the first step for me in creating it was to put in all the hard info and facts and then slowly transform it to what I want it to be. Vitorique's "slogan" is spark every hour and the idea is that the product will be used by people who are busy having too much fun in life so they don't have time to cook so they choose to have Vitorique. For example a commercial we are producing starts with first person footage of me getting in a skyrover 40 and then doing all sorts of water sports and having fun in the beach. At the end, there's a hot girl in a boat making a vitorique and drinking it. So as you can see it's not about the product itself but what we want people to feel when they think about it and part of what they feel will be conveyed by the logo.

I want to convey a sense of energy and fun. I want people to feel inspired and feel something when they see the packaging since this is the same logo that will go on the product packaging (I will hold another project for that as soon as this one ends).

Our target market is a young professional probably with higher disposable income than your average 24-35 year old, trendy, modern, sophisticated and often consumes premium brands and therefore the packaging must reflect that.

The bottle will use a shrink sleeve that will wrap around from the bottom of the bottle up to the neck. The bottle is white, with a white smooth cap. I want the design to be able to blend in with the white of the bottle so that it all flows. I was thinking of maybe leaving some parts transparent so that the white of the bottle shows instead of using white but I honestly don't know if that would be a good idea.

Attached you will find the template for the shrink sleeve, the logo and the tub. The picture of the bottle is only a reference so that you can know what size it will be.

I'm going to need the design both in the template and on the tub. Make it look nice since I might be using the designs as a background in the website and definitely as the product image (what people will be clicking on to buy it)

Here are the things that need to be on the tub (these will be modified later only to be used as a placeholder for now):

Under the logo or in the front and middle of the tub (under Vitorique probably):
A Complete and Balanced Meal Alternative.

It needs to say its vanilla flavored

It needs to have the supplement facts (just put any random numbers)

Directions: Use 2-4 scoops depending on your level of hunger. Mix 5 ounces of water per scoop in a thermos, shaker cup, or closed bottle and shake vigorously for ten seconds. Drink and enjoy!

What is Vitorique?
Vitorique is a complete and balanced meal alternative that gives your body all the right nutrients to keep it functioning at its full potential. Vitorique will nourish your body with good proteins, carbohydrates, fats, and micro-nutrients (like vitamins and minerals) so that you don't have to worry about cooking or eating the right stuff. We take care of everything for you so that you can keep on doing what you love, whatever that may be. Vitorique will spark every hour!
For more information go to Vitorique.com

Hey i forgot to add that its gonna be vanilla flavored

```html
<!DOCTYPE html>
<html lang="en">
<head>
<meta charset="utf-8">
<title>Vitorique – Meal Alternative Sleeve</title>
<link rel="stylesheet" href="https://fonts.googleapis.com/css2?family=Montserrat:ital,wght@0,400;0,500;0,600;0,700;0,800;1,600&display=swap">
<style>
  :root {
    --bg: #e4e4e4;
    --label-white: #f7f7f7;
    --brand-blue: #2a7fd0;
    --pill-blue: #2f8ad8;
    --badge-blue: #4aa3e6;
    --badge-light: #8cc8f2;
    --orange: #ee6a2c;
    --orange-deep: #d8431a;
    --ink: #222222;
    --rule: #333333;
    --white: #ffffff;
  }
  * { margin: 0; padding: 0; box-sizing: border-box; }
  html, body {
    width: 1200px; height: 960px; overflow: hidden;
    background: var(--bg);
    font-family: "Montserrat", Arial, sans-serif;
  }
  .sleeve {
    position: absolute; left: 40px; top: 215px;
    width: 1120px; height: 530px;
    background: var(--label-white);
    box-shadow: 0 10px 30px rgba(0,0,0,0.12);
    display: flex;
  }
  .panel { position: relative; height: 530px; overflow: hidden; }
  .panel--side { width: 320px; padding: 26px 24px; color: var(--ink); }
  .panel--front { width: 480px; }

  /* Left side: directions */
  .directions__title { font-size: 16px; font-weight: 800; color: var(--orange); letter-spacing: 1px; text-transform: uppercase; margin-bottom: 10px; }
  .directions__text { font-size: 12.5px; font-weight: 500; line-height: 1.6; }
  .directions__step { display: flex; gap: 10px; margin-top: 14px; font-size: 12px; font-weight: 600; line-height: 1.4; }
  .directions__num { flex: none; width: 24px; height: 24px; border-radius: 50%; background: var(--pill-blue); color: var(--white); font-size: 12px; font-weight: 700; display: flex; align-items: center; justify-content: center; }
  .side-url { position: absolute; left: 24px; bottom: 28px; font-size: 13px; font-weight: 700; color: var(--brand-blue); }

  /* Right side: supplement facts + about */
  .facts { border: 1.5px solid var(--rule); padding: 6px 8px; font-size: 9.5px; line-height: 1.3; }
  .facts__title { font-size: 17px; font-weight: 800; line-height: 1.1; }
  .facts__serving { border-bottom: 5px solid var(--rule); padding: 3px 0 3px; }
  .facts__row { display: flex; justify-content: space-between; border-bottom: 0.75px solid var(--rule); padding: 1.5px 0; }
  .facts__row--head { font-weight: 700; border-bottom-width: 2px; }
  .facts__row--sub { padding-left: 10px; }
  .facts__row b { font-weight: 700; }
  .facts__note { font-size: 7.5px; line-height: 1.3; margin-top: 3px; }
  .about { margin-top: 12px; }
  .about__title { font-size: 12px; font-weight: 800; color: var(--orange); margin-bottom: 4px; }
  .about__text { font-size: 8.6px; font-weight: 500; line-height: 1.38; }
  .about__link { font-size: 8.6px; font-weight: 700; margin-top: 4px; color: var(--brand-blue); }

  /* Front */
  .front__band { position: absolute; left: 0; top: 0; width: 480px; height: 530px; }
  .brand { position: absolute; left: 36px; top: 38px; display: flex; align-items: center; gap: 14px; }
  .brand__dot { width: 64px; height: 64px; border-radius: 50%; background: var(--orange); }
  .brand__name { font-size: 38px; font-weight: 500; letter-spacing: 0.5px; color: var(--brand-blue); text-transform: uppercase; }
  .brand__tagline { position: absolute; right: 40px; top: 100px; font-size: 15px; font-weight: 600; font-style: italic; color: var(--orange-deep); }
  .headline { position: absolute; left: 0; right: 0; top: 140px; text-align: center; color: var(--orange); }
  .headline__kicker { font-size: 16px; font-weight: 600; }
  .headline__main { font-size: 31px; font-weight: 600; line-height: 1.2; margin-top: 2px; }
  .flavor {
    position: absolute; left: 84px; top: 221px; width: 296px; height: 46px;
    background: var(--pill-blue); border-radius: 6px;
    color: var(--white); font-size: 23px; font-weight: 700; letter-spacing: 0.5px;
    display: flex; align-items: center; justify-content: center;
  }
  .benefits { position: absolute; left: 38px; top: 382px; list-style: none; color: var(--white); font-size: 12px; font-weight: 700; }
  .benefits li { margin-bottom: 9px; }
  .benefits li::before { content: "•"; margin-right: 8px; }
  .badge { position: absolute; left: 290px; top: 320px; width: 130px; height: 130px; }
  .footer { position: absolute; left: 0; right: 0; top: 490px; text-align: center; color: var(--white); }
  .footer__title { font-size: 14px; font-weight: 700; letter-spacing: 2px; }
  .footer__small { font-size: 6.5px; font-weight: 600; letter-spacing: 0.6px; margin-top: 6px; }
</style>
</head>
<body>
  <main class="sleeve">
    <section class="panel panel--side directions">
      <h2 class="directions__title">Directions</h2>
      <p class="directions__text">Use 2-4 scoops depending on your level of hunger.</p>
      <div class="directions__step"><span class="directions__num">1</span><span>Mix 5 ounces of water per scoop in a thermos, shaker cup, or closed bottle.</span></div>
      <div class="directions__step"><span class="directions__num">2</span><span>Shake vigorously for ten seconds.</span></div>
      <div class="directions__step"><span class="directions__num">3</span><span>Drink and enjoy!</span></div>
      <p class="side-url">Vitorique.com</p>
    </section>

    <section class="panel panel--front">
      <svg class="front__band" viewBox="0 0 480 530" aria-hidden="true">
        <defs>
          <linearGradient id="bandGradient" x1="0" y1="0" x2="1" y2="0">
            <stop offset="0" stop-color="#e8552a"/>
            <stop offset="0.45" stop-color="#f58a48"/>
            <stop offset="1" stop-color="#d8431a"/>
          </linearGradient>
        </defs>
        <path d="M0 330 C 110 312, 190 350, 300 318 S 440 282, 480 290 L480 530 L0 530 Z" fill="url(#bandGradient)"/>
      </svg>

      <div class="brand">
        <span class="brand__dot"></span>
        <span class="brand__name">Vitorique</span>
      </div>
      <div class="brand__tagline">Spark Every Hour!</div>

      <div class="headline">
        <p class="headline__kicker">A Complete and Balanced</p>
        <p class="headline__main">Meal Alternative</p>
      </div>
      <div class="flavor">VANILLA FLAVORED</div>

      <ul class="benefits">
        <li>Lorem ipsum dolor sit amet</li>
        <li>Lorem ipsum dolor sit amet, sit</li>
        <li>Lorem ipsum dolor sit ametsit sit</li>
        <li>Lorem ipsum dolor sit ametsit sit sit</li>
      </ul>

      <svg class="badge" viewBox="0 0 130 130">
        <g transform="translate(65 65)">
          <rect x="-46" y="-46" width="92" height="92" fill="var(--badge-blue)"/>
          <rect x="-46" y="-46" width="92" height="92" fill="var(--badge-blue)" transform="rotate(22.5)"/>
          <rect x="-46" y="-46" width="92" height="92" fill="var(--badge-blue)" transform="rotate(45)"/>
          <rect x="-46" y="-46" width="92" height="92" fill="var(--badge-blue)" transform="rotate(67.5)"/>
          <circle r="44" fill="var(--badge-light)"/>
          <g transform="rotate(-22)" fill="var(--white)" text-anchor="middle" font-family="Montserrat, Arial, sans-serif" font-weight="800">
            <text y="-2" font-size="22">YOUR</text>
            <text y="18" font-size="11">TEXT HERE!</text>
          </g>
        </g>
      </svg>

      <div class="footer">
        <p class="footer__title">LOREM IPSUM DOLOR SIT AMET</p>
        <p class="footer__small">LOREM IPSUM DOLOR SIT AMET, CONSECTETUR ADIPISICING ELIT, SED DO EIUSMOD TEMPO</p>
      </div>
    </section>

    <section class="panel panel--side">
      <div class="facts">
        <h2 class="facts__title">Supplement Facts</h2>
        <div class="facts__serving">Serving Size 2 Scoops (60 g)<br>Servings Per Container 15</div>
        <div class="facts__row facts__row--head"><span>Amount Per Serving</span><span>% Daily Value</span></div>
        <div class="facts__row"><span><b>Calories</b> 240</span><span></span></div>
        <div class="facts__row"><span><b>Total Fat</b> 8 g</span><span>10%</span></div>
        <div class="facts__row facts__row--sub"><span>Saturated Fat 1.5 g</span><span>8%</span></div>
        <div class="facts__row"><span><b>Sodium</b> 180 mg</span><span>8%</span></div>
        <div class="facts__row"><span><b>Total Carbohydrate</b> 28 g</span><span>10%</span></div>
        <div class="facts__row facts__row--sub"><span>Dietary Fiber 5 g</span><span>18%</span></div>
        <div class="facts__row"><span><b>Protein</b> 18 g</span><span>36%</span></div>
        <div class="facts__row"><span>Vitamin D 5 mcg · Calcium 260 mg</span><span>25%</span></div>
        <div class="facts__row"><span>Iron 4 mg · Potassium 470 mg</span><span>20%</span></div>
        <p class="facts__note">* Percent Daily Values are based on a 2,000 calorie diet.</p>
      </div>
      <div class="about">
        <h3 class="about__title">What is Vitorique?</h3>
        <p class="about__text">Vitorique is a complete and balanced meal alternative that gives your body all the right nutrients to keep it functioning at its full potential. Vitorique will nourish your body with good proteins, carbohydrates, fats, and micro-nutrients (like vitamins and minerals) so that you don't have to worry about cooking or eating the right stuff. We take care of everything for you so that you can keep on doing what you love, whatever that may be. Vitorique will spark every hour!</p>
        <p class="about__link">For more information go to Vitorique.com</p>
      </div>
    </section>
  </main>
</body>
</html>
```